Business Card Design Project

I run holistic health workshops, speaking engagements, group and 1on1 coaching, cooking classes, and am a speaker and presenter on holistic health topics.

I would like professionally designed business cards using the attached logo. I would like the reverse of the cards to use the leaf pattern blown up large across the back of the card as the design. I'd also like to use the words "mind.body.spirit.nutrition" across the backside of the cards.

The front of the cards should contain the following contact details:
Megan Thorsby-Quill
Founder & President
The Quill Consulting Group
+61 455 903 671
thequillconsultinggroup@mailvessel.example

Target Market(s)

Corporate HR, Health & wellness businesses, upmarket spas, other businesses in the holistic health & wellness fields looking for a speaker/presenter/workshop leader

Industry/Entity Type

Cooking

Requirements
Must have
• Must use the attached design; must use earth tones in line with the logo (browns/greens/blues/tans)

```html
<!DOCTYPE html>
<html lang="en">
<head>
<meta charset="utf-8">
<title>The Quill Consulting Group – Business Card</title>
<link rel="stylesheet" href="https://fonts.googleapis.com/css2?family=Questrial&family=Mulish:wght@700&display=swap">
<style>
  :root {
    --canvas: #ffffff;
    --card: #ffffff;
    --card-edge: #cfcfcf;
    --band: #d5e7b2;
    --ink: #333333;
    --ink-soft: #3d3d3d;
    --accent: #4caf3a;
    --leaf-light: #cfe3a6;
    --leaf-mid: #9ccc6c;
    --leaf-deep: #4fb57c;
  }
  * { margin: 0; padding: 0; box-sizing: border-box; }
  html, body {
    width: 1086px;
    height: 1200px;
    overflow: hidden;
    background: var(--canvas);
  }
  body {
    position: relative;
    font-family: "Questrial", "Century Gothic", sans-serif;
    color: var(--ink);
  }
  .card {
    position: absolute;
    left: 49px;
    width: 994px;
    height: 553px;
    background: var(--card);
    border: 1.5px solid var(--card-edge);
    box-shadow: 0 3px 10px rgba(0, 0, 0, 0.12);
    overflow: hidden;
  }
  .card--front { top: 18px; }
  .card--back { top: 608px; }

  .brand {
    position: absolute;
    top: 38px;
    left: 0;
    width: 100%;
    display: flex;
    justify-content: center;
    align-items: center;
    gap: 16px;
  }
  .brand__dot {
    width: 34px;
    height: 34px;
    border-radius: 50%;
    background: var(--accent);
  }
  .brand__name {
    font-size: 64px;
    line-height: 1;
    color: var(--ink-soft);
  }

  .band {
    position: absolute;
    left: 0;
    width: 100%;
    background: var(--band);
    display: flex;
    justify-content: center;
    align-items: center;
    color: var(--ink-soft);
  }
  .band--company {
    top: 172px;
    height: 53px;
    font-size: 42px;
  }

  .contact {
    position: absolute;
    top: 270px;
    left: 0;
    width: 100%;
    text-align: center;
  }
  .contact__name {
    font-family: "Mulish", "Century Gothic", sans-serif;
    font-weight: 700;
    font-size: 34px;
    color: var(--ink);
  }
  .contact__role {
    margin-top: 12px;
    font-size: 30px;
  }
  .contact__phone {
    margin-top: 36px;
    font-size: 31px;
    display: flex;
    justify-content: center;
    align-items: center;
    gap: 10px;
  }
  .contact__phone svg { width: 24px; height: 24px; }
  .contact__email {
    margin-top: 26px;
    font-size: 30px;
  }

  .motif {
    position: absolute;
    left: 232px;
    top: 10px;
    width: 543px;
    height: 390px;
    border-radius: 50% 50% 46% 46%;
    background: radial-gradient(ellipse at 50% 55%, var(--leaf-deep) 0%, var(--leaf-mid) 45%, var(--leaf-light) 72%, rgba(207, 227, 166, 0) 100%);
  }

  .band--tagline {
    top: 459px;
    height: 55px;
    font-size: 54px;
    gap: 14px;
  }
  .tagline__sep {
    width: 14px;
    height: 14px;
    border-radius: 50%;
    background: var(--accent);
    margin-top: 6px;
  }
</style>
</head>
<body>
  <section class="card card--front">
    <div class="brand">
      <span class="brand__dot"></span>
      <span class="brand__name">TQC Group</span>
    </div>
    <div class="band band--company">The Quill Consulting Group</div>
    <div class="contact">
      <p class="contact__name">Megan Thorsby-Quill</p>
      <p class="contact__role">Founder &amp; President</p>
      <p class="contact__phone">
        <svg viewBox="0 0 24 24" aria-hidden="true">
          <path d="M6.6 2.5c.6-.3 1.3 0 1.6.6l1.6 3.6c.3.6.1 1.2-.4 1.6l-1.5 1.1c.9 2 2.4 3.7 4.4 4.8l1.2-1.4c.4-.5 1.1-.6 1.6-.3l3.5 1.8c.6.3.8 1 .6 1.6l-.8 2.4c-.3.8-1 1.3-1.9 1.2C9.7 18.8 4.8 13.6 4.5 6.8c0-.8.4-1.5 1.1-1.8z" fill="none" stroke="#333" stroke-width="1.6" stroke-linejoin="round"/>
        </svg>
        +61 455 903 671
      </p>
      <p class="contact__email">thequillconsultinggroup@mailvessel.example</p>
    </div>
  </section>

  <section class="card card--back">
    <div class="motif" role="img" aria-label="Large layered leaf emblem of the consulting group in soft greens"></div>
    <div class="band band--tagline">
      <span>mind</span><span class="tagline__sep"></span>
      <span>body</span><span class="tagline__sep"></span>
      <span>spirit</span><span class="tagline__sep"></span>
      <span>nutrition</span>
    </div>
  </section>
</body>
</html>
```